Funky Modern Flyer A5 or Postcard size

Hi, I am looking at a one small flyer (A5 or postcard size) that I can put both on my website on the front page (ie so png) and also send out if necessary.

It has to be modern, funky and hip. My brand is professional / Corporate so it also has to fit in with that brand.

There are 6 attachments:
Example 1 - FernaPeak - I like this look, clean, modern, funky and says it all.
Example 2 - FernPeak - again another look I like, simple, explanatory
Example 4 - Brightstall Bazaar - font is cool on this one but background not so much too much going on but I like the font
Example 5 - Example 4 - Brightstall Bazaar - font is cool on this one but background not so much too much going on but I like the font
5 is my logo
Example 6 is something I found on the web this morning which is effective.

It is for a Mentoring and Training program I run called: HIGHSTRIDE

What is to be included is the following:
The name: Highstride
Somewhere: Training, Mentoring
My Logo (see attached two options) you can choose which colour suits and I have the source file should you need it
My website and email: www.miriambaskell.example / miriam@miriambaskell.example

This wording: This is one of our highest in-demand programs and is based on a background and proven track record by Miriam in accelerating sales organisations and their people into stand out high performers. **(NOTE this wording in this paragraph may change and I am open to you changing if you think you can make it more effective!)

Colours: white, black and gold (those are our website colours).

I'd like the Highstride to really stand out.... I have included two fonts that I really like that I got off Brightstall Bazaar. However, feel free to suggest other fonts that you think cool or funky!
Updates

Hi everyone, just to add a note to the brief, I am not overly keen on pictures that are really busy. I only like a picture that is minimal and effective. The examples from Brightstall Bazaar was more for the Font Style not so much the pictures in the background. The pictures can take away from a design unless done really minimally.....hope this makes sense. Miriam Added Wednesday, March 15, 2017

Target Market(s)

My target Market is Corporates but I want a Funky Modern look as a lot of people in Corporates are Millennials as well which is part of my target market

Industry/Entity Type

Information Technology

Requirements
Must have
• What is to be included is the following:
• The name: Highstride
• Somewhere: Training, Mentoring
• My Logo (see attached two options) you can choose which colour suits and I have the source file should you need it
• My website and email: www.miriambaskell.example / miriam@miriambaskell.example
• This wording: This is one of our highest in-demand programs and is based on a background and proven track record in high performance and accelerating sales organisations and their people into stand out high performers. (**NOTE this wording may change when final design is picked to be changed as still working in it***)
• Colours: white, black and gold (those are our website colours).
• I'd like the Highstride to really stand out.... I have included two fonts that I really like that I got off Brightstall Bazaar. However, feel free to suggest other fonts that you think cool or funky! NOTE: The pictures I have attached is mainly for the FONTS not for the background pictures. I am not that keen on background pictures as it can take away from the font - unless it is minimal
Should not have
• Too many different colours, I like slick, modern, clean. White, gold and black preferred as this is our website colour.
• NOTE: The pictures from Brightstall Bazaar I have attached are mainly for the FONTS not for the background pictures. I am not hugely keen on background pictures as it can take away from the font/message - unless the pictures are minimal but effective.

```html
<!DOCTYPE html>
<html lang="en">
<head>
<meta charset="utf-8">
<title>Highstride – Training &amp; Mentoring Flyer</title>
<link rel="stylesheet" href="https://fonts.googleapis.com/css2?family=Kaushan+Script&family=Yellowtail&family=Open+Sans:wght@400;700&family=Raleway:wght@400&family=Oswald:wght@600&display=block">
<style>
  :root {
    --gold-light: #f6dc86;
    --gold: #d9a91f;
    --gold-deep: #b98a12;
    --ink: #000000;
    --paper: #ffffff;
    --text-light: #f4f4f4;
    --map-blue: #6fb4e8;
    --map-blue-deep: #3d86c6;
  }
  html, body {
    margin: 0;
    padding: 0;
    width: 846px;
    height: 1200px;
    overflow: hidden;
    background: var(--paper);
  }
  .flyer {
    position: relative;
    width: 846px;
    height: 1200px;
    overflow: hidden;
    background: linear-gradient(180deg, #ffffff 0%, #e2e2e2 18%, #bcbcbc 42%, #8a8a8a 60%, #3c3c3c 75%, #0d0d0d 88%, #000000 100%);
    font-family: "Open Sans", Arial, sans-serif;
  }
  .corner-ribbon {
    position: absolute;
    top: 0;
    left: 0;
    width: 846px;
    height: 300px;
  }
  .corner-ribbon text {
    font-family: "Oswald", "Arial Narrow", sans-serif;
    font-weight: 600;
    font-size: 38px;
    letter-spacing: 1px;
    fill: var(--ink);
  }
  .hero-illustration {
    position: absolute;
    left: 115px;
    top: 185px;
    width: 620px;
    height: 350px;
    background:
      radial-gradient(ellipse closest-side at 62% 62%, var(--map-blue) 0%, var(--map-blue-deep) 55%, rgba(61,134,198,0) 100%),
      radial-gradient(ellipse closest-side at 50% 50%, rgba(20,20,20,0.55) 0%, rgba(20,20,20,0.35) 60%, rgba(20,20,20,0) 100%);
  }
  .program-title {
    position: absolute;
    left: 0;
    right: 0;
    top: 605px;
    margin: 0;
    text-align: center;
    font-family: "Yellowtail", "Kaushan Script", cursive;
    font-weight: 400;
    font-size: 190px;
    line-height: 1;
    color: var(--gold);
    background: linear-gradient(100deg, var(--gold-deep) 0%, var(--gold) 30%, var(--gold-light) 60%, var(--gold) 85%, var(--gold-deep) 100%);
    -webkit-background-clip: text;
    background-clip: text;
    -webkit-text-fill-color: transparent;
    filter: drop-shadow(3px 5px 4px rgba(0,0,0,0.55));
  }
  .program-summary {
    position: absolute;
    left: 40px;
    right: 40px;
    top: 838px;
    margin: 0;
    text-align: center;
    color: var(--text-light);
    font-size: 22px;
    line-height: 30px;
  }
  .brand-name {
    position: absolute;
    left: 0;
    right: 0;
    top: 1082px;
    margin: 0;
    text-align: center;
    font-family: "Raleway", Arial, sans-serif;
    font-weight: 400;
    font-size: 38px;
    letter-spacing: 2px;
    color: var(--gold);
  }
  .contact-line {
    position: absolute;
    left: 0;
    right: 0;
    top: 1138px;
    margin: 0;
    display: flex;
    justify-content: center;
    gap: 30px;
    color: var(--text-light);
    font-size: 20px;
  }
  .contact-label {
    color: var(--gold);
    font-weight: 700;
    font-size: 16px;
    margin-right: 8px;
  }
</style>
</head>
<body>
  <main class="flyer">
    <svg class="corner-ribbon" viewBox="0 0 846 300" aria-hidden="true">
      <defs>
        <linearGradient id="ribbonGold" x1="0" y1="0" x2="1" y2="1">
          <stop offset="0" stop-color="#f8e39a"/>
          <stop offset="0.5" stop-color="#e2b73a"/>
          <stop offset="1" stop-color="#c4931a"/>
        </linearGradient>
      </defs>
      <polygon points="545,0 846,0 846,296" fill="url(#ribbonGold)"/>
      <text x="737" y="86" text-anchor="middle" transform="rotate(45 737 86)">TRAINING</text>
      <text x="718" y="130" text-anchor="middle" transform="rotate(45 718 130)">MENTORING</text>
    </svg>

    <div class="hero-illustration" role="img" aria-label="Illustration of business people in silhouette standing on a blue world map with a curved arrow"></div>

    <h1 class="program-title">Highstride</h1>

    <p class="program-summary">This is one of our highest in-demand programs and is based on a back-ground and proven track record by Miriam in accelerating sales organi-sations and their people into stand out high performers.</p>

    <p class="brand-name">MIRIAM BASKELL</p>

    <p class="contact-line">
      <span><span class="contact-label">W</span>www.miriambaskell.example</span>
      <span><span class="contact-label">E</span>miriam@miriambaskell.example</span>
    </p>
  </main>
</body>
</html>
```